Talvane Companies Business Card Design

We need a new business card for our Private Equity Real Estate Development firm, “Talvane” and our EB-5 regional center “Moorfield Regional Center” on one card. We prefer a design that is simple, elegant, and represents the luxury products we design and build as well as the financial security and stability our successful history has produced. We are an industry leader in our field and 3rd generation family business that has evolved into an institutional quality investment platform. Considered design size is standard business card dimensions (3.5 x 2 inches with an additional 1/8 inch space for design elements or backgrounds that extend beyond the finished size of your piece.

Target Market(s)

• High net worth individuals
• Highly skilled technical workers and physicians in the US seeking investment-based immigration opportunities
• Sophisticated private equity investors
• Intermediary partners include domestic attorneys and investment brokers, as well as international agent networks
• US real estate developers

Industry/Entity Type

Finance

Contact Information for Business Card

(Providing placeholder info for personal information, please design for longer character spaces, longer names and addresses etc..)
• Logo for Talvane
• Logo for Moorfield Regional Center
• Full name: Dorian Talvane
• Job title: CEO
• Email address: dtalvane@talvanecompanies.example
• Cell phone number: +1.555.318.4476
• Office number +1.555.240.6185
• Office address: Quillan Court 5, 4817 Vista Ardell, Larkmont, NV.
• Website: www.talvanecompanies.example

Font styles to use
Serif
Sans Serif

Colors
ec1f27
ffffff
000000

Requirements
Must have
• • Logo for Talvane
• • Logo for Moorfield Regional Center
• - Use rounded corners
• (See .ai file included for logos)
Nice to have
• • Simple, elegant design
• • Aesthetically compatible with our website design (www.talvanecompanies.example)
• • Color palette including but not limited to white, black, and red (as per logos)
Should not have
• - Not too much red color
• - Do not stack both logos on top of each other

```html
<!DOCTYPE html>
<html lang="en">
<head>
<meta charset="utf-8">
<title>Talvane Companies Business Card</title>
<link rel="stylesheet" href="https://fonts.googleapis.com/css2?family=Cinzel:wght@700&family=Lato:wght@400&display=swap">
<style>
  :root {
    --backdrop: #656565;
    --card: #2f2f2f;
    --red: #a81d2e;
    --white: #ffffff;
    --mark-grey: #4a4a4a;
    --rule: #4a2a2d;
  }
  * { margin: 0; padding: 0; box-sizing: border-box; }
  html, body { width: 1200px; height: 1200px; overflow: hidden; }
  body { background: var(--backdrop); position: relative; font-family: "Lato", sans-serif; }

  .card {
    position: absolute;
    left: 246px;
    width: 708px;
    height: 404px;
    background: var(--card);
    border-radius: 26px;
    overflow: hidden;
  }
  .card--front { top: 138px; }
  .card--back { top: 663px; }

  /* Front */
  .front-brand {
    position: absolute;
    top: 50%; left: 50%;
    transform: translate(-50%, -50%);
    display: flex; align-items: center; gap: 18px;
    white-space: nowrap;
  }
  .front-brand__square { width: 64px; height: 64px; background: var(--red); flex: none; }
  .front-brand__name {
    font-family: "Cinzel", serif; font-weight: 700;
    font-size: 40px; color: var(--mark-grey); letter-spacing: 1px;
    white-space: nowrap;
  }

  /* Back: regional center */
  .center-brand {
    position: absolute; right: 36px; top: 44px;
    width: 240px; text-align: center;
    color: var(--red);
  }
  .center-brand__square { width: 56px; height: 56px; background: var(--red); margin: 0 auto 22px; }
  .center-brand__name {
    font-family: "Cinzel", serif; font-weight: 700;
    font-size: 34px; line-height: 1; white-space: nowrap;
  }
  .center-brand__sub {
    font-family: "Lato", sans-serif;
    font-size: 12px; letter-spacing: 6px; margin-top: 6px;
    text-transform: uppercase; white-space: nowrap;
  }

  /* Back: person */
  .person { position: absolute; left: 38px; top: 210px; }
  .person__name {
    font-family: "Cinzel", serif; font-weight: 700;
    font-size: 26px; color: var(--red); line-height: 32px; white-space: nowrap;
  }
  .person__title { font-size: 18px; color: var(--white); line-height: 26px; }

  .divider {
    position: absolute; left: 38px; right: 36px; top: 279px;
    height: 1px; background: var(--rule);
  }

  .contacts { position: absolute; left: 38px; top: 296px; list-style: none; }
  .contacts li {
    display: flex; align-items: center; gap: 12px;
    font-size: 17px; color: var(--white); height: 23.5px; white-space: nowrap;
  }
  .contacts svg { width: 18px; height: 16px; fill: var(--red); flex: none; }

  .address {
    position: absolute; right: 36px; top: 316px;
    text-align: right; font-size: 17px; color: var(--white); line-height: 25px;
    white-space: nowrap;
  }

  .footer-band { position: absolute; left: 0; bottom: 0; width: 708px; height: 34px; }
  .website {
    position: absolute; right: 36px; bottom: 6px;
    font-size: 17px; color: var(--white); white-space: nowrap;
  }
</style>
</head>
<body>

<section class="card card--front">
  <div class="front-brand">
    <span class="front-brand__square"></span>
    <span class="front-brand__name">Talvane Capital</span>
  </div>
</section>

<section class="card card--back">
  <div class="center-brand">
    <div class="center-brand__square"></div>
    <div class="center-brand__name">Moorfield</div>
    <div class="center-brand__sub">Regional Center</div>
  </div>

  <div class="person">
    <div class="person__name">Dorian Talvane</div>
    <div class="person__title">CEO</div>
  </div>

  <div class="divider"></div>

  <ul class="contacts">
    <li>
      <svg viewBox="0 0 18 16" aria-hidden="true"><path d="M4 1l3 3-1.6 2c1 2 2.6 3.6 4.6 4.6L12 9l3 3-2 2.5C7.5 14 2.5 9 2 3z"/></svg>
      +1.555.318.4476
    </li>
    <li>
      <svg viewBox="0 0 18 16" aria-hidden="true"><path d="M5 0h8v16H5z M6.5 1.5v11h5v-11z"/></svg>
      +1.555.240.6185
    </li>
    <li>
      <svg viewBox="0 0 18 16" aria-hidden="true"><path d="M1 3h16v1L9 9 1 4z M1 6l8 5 8-5v7H1z"/></svg>
      dtalvane@talvanecompanies.example
    </li>
  </ul>

  <div class="address">
    Quillan Court 5, 4817 Vista Ardell<br>
    Larkmont, NV
  </div>

  <svg class="footer-band" viewBox="0 0 708 34" preserveAspectRatio="none" aria-hidden="true">
    <polygon points="0,4 392,4 386,12 0,12" fill="var(--red)"/>
    <polygon points="0,20 378,20 372,34 0,34" fill="var(--red)"/>
    <polygon points="404,0 708,0 708,34 380,34" fill="var(--red)"/>
  </svg>
  <div class="website">www.talvanecompanies.example</div>
</section>

</body>
</html>
```